Harbor of Bright Morning Paths, LLC needs business stationary designed using our logo.

Harbor of Bright Morning Paths is a new life coaching business. We have a logo design . We need a design for stationary for branding a new PathCrafter Life Coach business. We help people transform their lives by exploring, designing and taking action steps for the life they love in the areas of health and wellness, relationships, vocation, and time and money freedom. We like bright happy colors that present growth and transformation and also compliments the blue logo design.

Hello Designers, Thank you for accepting my design request. I wanted to be sure I put all the information for the business stationary design. If this is already in the order please disregard. Information to incorporate into stationary design Logo: incorporate blues and complimentary color Company name: Harbor of Bright Morning Paths, LLC Tagline: Transformational Life Coaching "If you can think it, you can do it You CAN live a life you LOVE! Website: www.norasaltwell.PathCrafterGuide.com Email: norasaltwell@PathCrafterGuide.com P.O. Box 5293 Edcouch, TX 78538 555-017-392 Nora T. Saltwell, Certified PathCrafter* Coach Positive, upbeat, professional design Thank you.

Industry/Entity Type

Life Coaching

Font styles to use
Decorative

Colors
0355a3

Requirements
Must have
• Information to incorporate into stationary design
• Logo: incorporate blues and complimentary color
• Company name: Harbor of Bright Morning Paths, LLC
• Tagline: Transformational Life Coaching
• "If you can think it, you can do it You CAN live a life you LOVE!
• Website: www.norasaltwell.PathCrafterGuide.com
• Email: norasaltwell@PathCrafterGuide.com
• P.O. Box 5293 Edcouch, TX 78538 555-017-392
• Nora T. Saltwell, Certified PathCrafter* Coach
• Positive, upbeat, professional design
Nice to have
• Watermark
Should not have
• No negativity or negative vibes
• Nothing derogatory
• No clashing colors

```html
<!DOCTYPE html>
<html lang="en">
<head>
<meta charset="utf-8">
<title>Harbor of Bright Morning Paths, LLC – Business Cards</title>
<link rel="stylesheet" href="https://fonts.googleapis.com/css2?family=Cormorant+Garamond:wght@700&family=Montserrat:wght@400;500;700&display=swap">
<style>
  :root {
    --page-bg: #eeece8;
    --brand-blue: #0b47a0;
    --deep-blue: #1a2a8f;
    --logo-violet: #3a1fc4;
    --gold: #e9a41d;
    --card-white: #ffffff;
    --text-dark: #1f1f1f;
    --text-grey: #6b6b6b;
  }
  * { box-sizing: border-box; margin: 0; padding: 0; }
  html, body {
    width: 1200px; height: 790px; overflow: hidden;
    background: var(--page-bg);
  }
  .stage { position: relative; width: 1200px; height: 790px; }

  .card {
    position: absolute;
    width: 540px; height: 310px;
    border-radius: 18px;
    box-shadow: 0 8px 22px rgba(0,0,0,.18);
    overflow: hidden;
  }

  /* Front */
  .card-front { left: 50px; top: 110px; background: var(--brand-blue); }
  .front-mark {
    position: absolute; left: 34px; top: 54px;
    display: flex; align-items: center; gap: 14px;
  }
  .mark-circle {
    flex: none;
    width: 150px; height: 150px; border-radius: 50%;
    background: radial-gradient(circle at 40% 40%, #4a2ad8, var(--logo-violet) 60%, #2a148f);
  }
  .mark-name {
    font-family: "Montserrat", sans-serif; font-weight: 700;
    font-size: 15px; line-height: 1.3; color: var(--card-white);
    width: 150px;
  }
  .front-tagline {
    position: absolute; right: 36px; bottom: 34px;
    font-family: "Cormorant Garamond", serif; font-weight: 700;
    font-variant: small-caps; color: var(--gold);
    font-size: 23px; line-height: 1.05; text-align: left;
  }

  /* Back */
  .card-back {
    left: 610px; top: 370px; background: var(--card-white);
    font-family: "Montserrat", sans-serif;
  }
  .back-header {
    position: absolute; left: 36px; top: 44px;
    display: flex; align-items: center; gap: 14px;
  }
  .back-header .mark-circle { width: 70px; height: 70px; }
  .company-name { font-weight: 700; font-size: 14px; color: var(--deep-blue); }
  .company-tagline { font-weight: 500; font-size: 12.5px; color: var(--text-grey); margin-top: 3px; }

  .person { position: absolute; left: 36px; top: 150px; }
  .person-name {
    font-weight: 700; font-size: 18px; letter-spacing: .5px;
    color: var(--deep-blue); text-transform: uppercase;
  }
  .person-title { font-weight: 500; font-size: 11.5px; color: var(--text-dark); margin-top: 2px; }

  .contact {
    position: absolute; left: 36px; top: 212px;
    font-size: 11.5px; font-weight: 500; color: var(--text-dark); line-height: 1.45;
    border-left: 3px solid var(--gold); padding-left: 14px;
  }
  .contact p.gap { margin-top: 6px; }

  .social {
    position: absolute; right: 30px; top: 196px;
    display: flex; gap: 8px;
    font-size: 10px; font-weight: 700; color: var(--deep-blue);
  }
</style>
</head>
<body>
<main class="stage">

  <section class="card card-front" aria-label="Business card front">
    <div class="front-mark">
      <div class="mark-circle"></div>
      <span class="mark-name">Harbor of Bright Morning Paths</span>
    </div>
    <p class="front-tagline">Picture the path, then take the step<br>You CAN build a day you LOVE!</p>
  </section>

  <section class="card card-back" aria-label="Business card back">
    <header class="back-header">
      <div class="mark-circle"></div>
      <div>
        <h1 class="company-name">Harbor of Bright Morning Paths, LLC</h1>
        <p class="company-tagline">Transformational Coaching</p>
      </div>
    </header>

    <div class="person">
      <h2 class="person-name">Nora T. Saltwell</h2>
      <p class="person-title">Certified PathCrafter* Coach</p>
    </div>

    <div class="contact">
      <p>P.O. Box 5293 Larkmont, TX 70417</p>
      <p>555-017-392</p>
      <p class="gap">norasaltwell@PathCrafterGuide.com</p>
      <p>www.norasaltwell.PathCrafterGuide.com</p>
    </div>

    <nav class="social" aria-label="Social profiles">
      <span>Linkpage</span><span>Chirpline</span><span>Circlenet</span>
    </nav>
  </section>

</main>
</body>
</html>
```